International horse riding portal needs web design

We are looking for the web design for the new "Feldmoor" web portal.

Offers from the world of horses and riding should be found on this portal, eg from the categories riding schools, riding holidays, farriers, riding stables, riding stables. And all information about riding.

It is important that the different areas can be found easily and clearly. For some categories, some features should already be available in the search bar.

In addition, the design should make you want to go horse riding. The user should be emotionally picked up on the landing page.

In the lower area, some offers should be advertised, eg from the areas of riding holidays, riding training, and horse trading.

Please use the colors from the logo for the design.
C100 M50 Y10 K50 and C0 M20 Y60 K30

```html
<!DOCTYPE html>
<html lang="en">
<head>
<meta charset="utf-8">
<title>Feldmoor – Horses and Riding</title>
<link rel="stylesheet" href="https://fonts.googleapis.com/css2?family=Montserrat:wght@400;500;600;700&family=Enriqueta:wght@600;700&display=swap">
<style>
:root{
  --navy:#0b4279;
  --navy-deep:#073866;
  --gold:#b38d48;
  --gold-soft:#c9a465;
  --ink:#2b2b2b;
  --muted:#6d6d6d;
  --white:#ffffff;
  --line:#e2d6bf;
}
*{margin:0;padding:0;box-sizing:border-box}
html,body{width:1200px;height:2682px;overflow:hidden;background:var(--white)}
body{position:relative;font-family:'Montserrat',sans-serif;color:var(--ink)}
.abs{position:absolute}
.serif{font-family:'Enriqueta',serif}

/* header */
.brand{left:111px;top:40px;display:flex;align-items:center;gap:10px}
.brand-dot{width:22px;height:22px;border-radius:50%;background:var(--gold)}
.brand-name{font-family:'Enriqueta',serif;font-weight:700;font-size:34px;color:var(--navy);letter-spacing:1px}
.search{left:421px;top:20px;width:266px;height:48px;border-radius:24px;background:#fff;box-shadow:0 2px 8px rgba(0,0,0,.18);display:flex;align-items:center;padding:0 4px 0 20px;justify-content:space-between;color:#999;font-size:16px}
.search-btn{width:40px;height:40px;border-radius:50%;background:var(--navy);display:flex;align-items:center;justify-content:center}
.topnav{left:729px;top:32px;display:flex;gap:34px;font-size:18px;color:#444}
.topnav .active{color:var(--navy);font-weight:700}
.login{left:991px;top:20px;width:97px;height:48px;border-radius:24px;background:var(--gold);color:#fff;font-weight:600;font-size:17px;display:flex;align-items:center;justify-content:center;box-shadow:0 2px 6px rgba(0,0,0,.2)}
.rule{left:393px;top:91px;width:695px;height:1px;background:var(--line)}
.subnav{left:413px;top:112px;display:flex;font-size:18px;color:#333}
.subnav span{padding:0 26px;border-left:1px solid #ccc;line-height:22px}
.subnav span:first-child{padding-left:0;border-left:none}
.subnav span:last-child{padding-right:0}

/* hero */
.hero{left:0;top:158px;width:1200px;height:640px;background:linear-gradient(180deg,#ecd3d2 0%,#e3cdc4 35%,#c6a77a 70%,#b59466 100%)}
.hero-art{left:560px;top:175px;width:560px;height:390px;border-radius:6px;background:radial-gradient(ellipse at 40% 50%,#7a3c22 0%,#8a5a3d 40%,rgba(180,140,90,0) 75%)}
.welcome{left:160px;top:350px;width:333px;text-align:center;color:var(--navy)}
.welcome small{display:block;font-family:'Enriqueta',serif;font-weight:700;font-size:30px}
.welcome strong{display:block;font-family:'Enriqueta',serif;font-weight:700;font-size:62px;line-height:1.1;margin-top:6px}
.tabs{left:111px;top:561px;width:757px;height:64px;background:#fff;border-radius:14px 14px 0 0;display:flex;align-items:center;font-size:18px;font-weight:500;color:#222}
.tabs span{padding:0 24px;border-left:1px solid #ddd;line-height:36px}
.tabs .on{background:var(--navy);color:#fff;border-radius:14px 0 0 0;line-height:64px;padding:0 18px;border:none;font-weight:600}
.tabs .on + span{border-left:none;padding-left:14px}
.finder{left:111px;top:625px;width:977px;height:70px;background:#fff;border-radius:0 35px 35px 35px;box-shadow:0 4px 14px rgba(0,0,0,.12);display:flex;align-items:center;padding:0 17px 0 20px}
.opt{display:flex;align-items:center;gap:10px;font-size:18px;margin-right:28px}
.radio{width:22px;height:22px;border-radius:50%;background:#fff;box-shadow:0 1px 4px rgba(0,0,0,.25);display:flex;align-items:center;justify-content:center}
.radio.sel::after{content:"";width:11px;height:11px;border-radius:50%;background:var(--gold)}
.zip{margin-left:auto;width:300px;height:48px;border-radius:24px;box-shadow:0 2px 6px rgba(0,0,0,.15);display:flex;align-items:center;justify-content:space-between;padding:0 4px 0 28px;font-size:18px;color:#555}
.send{width:40px;height:40px;border-radius:50%;background:var(--navy);display:flex;align-items:center;justify-content:center}
.hero-curve{left:0;top:718px}

/* sections */
.title{left:0;width:1200px;text-align:center;font-family:'Enriqueta',serif;font-weight:700;font-size:36px;color:var(--navy)}
.divider{left:527px;width:146px}
.intro{left:111px;top:938px;width:977px;font-size:18px;line-height:30px;text-align:justify;text-align-last:center;color:#333}
.tile{border-radius:14px;overflow:hidden;border:2px solid var(--navy);color:#fff;font-weight:600;font-size:18px;display:flex;align-items:flex-end;justify-content:center;padding-bottom:26px}
.tile.lift{border:none;box-shadow:0 6px 16px rgba(0,0,0,.25)}
.arrow-btn{top:1226px;width:38px;height:38px}

.offer-img{top:1548px;width:309px;height:242px;border-radius:14px}
.offer{top:1737px;width:275px;height:241px;background:#fff;border-radius:14px;box-shadow:0 4px 14px rgba(0,0,0,.14);padding:38px 16px 0 16px}
.offer h3{font-size:17px;font-weight:700;color:var(--navy)}
.offer p{margin-top:18px;font-size:17.5px;line-height:28px;color:#333}
.offer .go{position:absolute;left:16px;bottom:20px}

/* footer */
.foot-wave{left:0;top:2038px}
.footer{left:0;top:2110px;width:1200px;height:572px;background:var(--navy)}
.foot-brand{left:111px;top:2218px;display:flex;align-items:center;gap:10px}
.foot-brand .brand-dot{background:#fff}
.foot-brand .brand-name{color:#fff}
.updates{left:731px;top:2176px;font-family:'Enriqueta',serif;font-weight:700;font-size:19px;color:#fff;letter-spacing:.3px}
.email{left:725px;top:2219px;width:363px;height:53px;border-radius:27px;background:#fff;display:flex;align-items:center;justify-content:space-between;padding:0 5px 0 30px;font-size:18px;color:#444}
.email .send{background:var(--gold);width:44px;height:44px}
.foot-rule{left:111px;width:977px;height:1px;background:rgba(255,255,255,.15)}
.col-h{top:2364px;font-family:'Enriqueta',serif;font-weight:700;font-size:16px;color:#fff;padding-bottom:10px;border-bottom:1px solid var(--gold)}
.contact{left:111px;color:#fff;font-size:14px;display:flex;gap:14px;align-items:flex-start;line-height:30px}
.about-text{left:419px;top:2420px;width:253px;font-size:14px;line-height:24px;color:#fff;text-align:justify}
.links{top:2416px;list-style:none;color:#fff;font-size:14px}
.links li{line-height:26px;display:flex;align-items:center;gap:14px}
.links li::before{content:"";width:5px;height:5px;border-radius:50%;background:#fff}
.follow{left:421px;top:2554px;display:flex;align-items:center;gap:28px}
.follow .col-h{position:static}
.social{display:flex;gap:12px}
.social span{width:32px;height:32px;border:1px solid var(--gold);border-radius:50%}
.copy{left:0;top:2627px;width:1200px;text-align:center;color:#fff;font-size:13px}
</style>
</head>
<body>

<!-- header -->
<div class="abs brand"><span class="brand-dot"></span><span class="brand-name">FELDMOOR</span></div>
<div class="abs search">Search...<span class="search-btn"><svg width="20" height="20" viewBox="0 0 20 20" fill="none" stroke="#fff" stroke-width="2"><circle cx="8.5" cy="8.5" r="6"/><path d="M13 13l5 5"/></svg></span></div>
<nav class="abs topnav"><span class="active">Home</span><span>About</span><span>My List</span></nav>
<div class="abs login">LOG IN</div>
<div class="abs rule"></div>
<nav class="abs subnav"><span>Riding schools</span><span>Riding holidays</span><span>Farriers</span><span>Riding stables</span><span>More</span></nav>

<!-- hero -->
<div class="abs hero" role="img" aria-label="Rider in a cowboy hat galloping a chestnut horse through a golden meadow with hills behind"></div>
<div class="abs hero-art" role="img" aria-label="Chestnut horse and rider in motion"></div>
<div class="abs welcome"><small>WELCOME TO</small><strong>FELDMOOR</strong></div>
<div class="abs tabs"><span class="on">Riding Schools</span><span>Riding Holidays</span><span>Farriers</span><span>Riding Stables</span><span>More</span></div>
<div class="abs finder">
  <div class="opt"><span class="radio sel"></span>Feature 1</div>
  <div class="opt"><span class="radio"></span>Feature 2</div>
  <div class="opt"><span class="radio"></span>Feature 3</div>
  <div class="opt"><span class="radio"></span>Feature 4</div>
  <div class="zip">Zip/City<span class="send"><svg width="16" height="16" viewBox="0 0 16 16"><path d="M15 1L1 7l6 2 2 6z" fill="#fff"/></svg></span></div>
</div>
<svg class="abs hero-curve" width="1200" height="82" viewBox="0 0 1200 82">
  <path d="M0 55 Q600 -25 1200 55 L1200 82 L0 82Z" fill="#fff"/>
  <path d="M0 62 Q600 -8 1200 75 L1200 82 Q600 18 0 82Z" fill="#b38d48"/>
</svg>

<!-- horses and riding -->
<h2 class="abs title" style="top:826px">HORSES AND RIDING</h2>
<svg class="abs divider" style="top:878px" width="146" height="24" viewBox="0 0 146 24"><path d="M0 2H146" stroke="#b38d48" stroke-width="2"/><path d="M57 7H89L73 22Z" fill="#b38d48"/></svg>
<p class="abs intro">Sed ut perspiciatis unde omnis iste natus error sit voluptatem accusantium doloremque laudantium, totam rem aperiam, eaque ipsa quae ab illo inventore veritatis et quasi architecto beatae vitae dicta sunt explicabo. Nemo enim ipsam voluptatem quia voluptas sit aspernatur aut odit aut fugit, sed quia consequuntur magni dolores eos qui ratione voluptatem sequi nesciunt. Neque porro quisquam est, qui dolorem ipsum quia dolor sit amet.</p>

<svg class="abs arrow-btn" style="left:34px" viewBox="0 0 38 38" fill="none" stroke="#9fb4cc" stroke-width="2"><circle cx="19" cy="19" r="17"/><path d="M27 19H11M17 13l-6 6 6 6"/></svg>
<div class="abs tile" style="left:111px;top:1130px;width:225px;height:227px;background:linear-gradient(180deg,#6f9a3c 0%,#8fae5a 40%,#3b6a9a 100%)" role="img" aria-label="Girl in a riding helmet on a pony among green trees"><span>Riding Schools</span></div>
<div class="abs tile lift" style="left:346px;top:1115px;width:256px;height:257px;background:linear-gradient(180deg,#b6e6e6 0%,#4cc4c4 45%,#2e6f9a 100%)" role="img" aria-label="Two riders on horses walking along a turquoise beach"><span>Riding Holidays</span></div>
<div class="abs tile" style="left:612px;top:1130px;width:226px;height:227px;background:linear-gradient(180deg,#9b8a70 0%,#c8c0b4 45%,#3b6a9a 100%)" role="img" aria-label="Farrier in a work apron at his workshop"><span>Farriers</span></div>
<div class="abs tile" style="left:862px;top:1130px;width:226px;height:227px;background:linear-gradient(180deg,#6b5a52 0%,#3a3230 50%,#2f5d8c 100%)" role="img" aria-label="Rider on a black horse inside a stable hall"><span>Riding Stables</span></div>
<svg class="abs arrow-btn" style="left:1122px" viewBox="0 0 38 38" fill="none" stroke="#0b4279" stroke-width="2"><circle cx="19" cy="19" r="17"/><path d="M11 19H27M21 13l6 6-6 6"/></svg>

<!-- riding holidays -->
<h2 class="abs title" style="top:1429px">RIDING HOLIDAYS</h2>
<svg class="abs divider" style="top:1482px" width="146" height="24" viewBox="0 0 146 24"><path d="M0 2H146" stroke="#b38d48" stroke-width="2"/><path d="M57 7H89L73 22Z" fill="#b38d48"/></svg>

<div class="abs offer-img" style="left:111px;background:linear-gradient(180deg,#cfd6da 0%,#a9b2b4 55%,#6b3a26 100%)" role="img" aria-label="Woman in a plaid shirt riding a horse under a cloudy sky"></div>
<div class="abs offer-img" style="left:445px;background:linear-gradient(135deg,#3a2418 0%,#9c6a44 50%,#4a2c1c 100%)" role="img" aria-label="Horse looking out over its stable door"></div>
<div class="abs offer-img" style="left:780px;background:linear-gradient(135deg,#2f4a6a 0%,#e6b86a 50%,#3a2a24 100%)" role="img" aria-label="Woman grooming a dark horse in a stable aisle"></div>

<div class="abs offer" style="left:128px"><h3>LAND | REAGION</h3><p>Udi officipsamus dolut alici fugit faceseq uodisquati fugi sunte mod eum id utterzdy ullatquam aceat.</p><svg class="go" width="28" height="20" viewBox="0 0 28 20"><circle cx="10" cy="10" r="9" fill="#b38d48"/><path d="M8 10H25M20 5l5 5-5 5" stroke="#0b4279" stroke-width="2.2" fill="none"/></svg></div>
<div class="abs offer" style="left:462px"><h3>LAND | REAGION</h3><p>Udi officipsamus dolut alici fugit faceseq uodisquati fugi sunte mod eum id utterzdy ullatquam aceat.</p><svg class="go" width="28" height="20" viewBox="0 0 28 20"><circle cx="10" cy="10" r="9" fill="#b38d48"/><path d="M8 10H25M20 5l5 5-5 5" stroke="#0b4279" stroke-width="2.2" fill="none"/></svg></div>
<div class="abs offer" style="left:797px"><h3>LAND | REAGION</h3><p>Udi officipsamus dolut alici fugit faceseq uodisquati fugi sunte mod eum id utterzdy ullatquam aceat.</p><svg class="go" width="28" height="20" viewBox="0 0 28 20"><circle cx="10" cy="10" r="9" fill="#b38d48"/><path d="M8 10H25M20 5l5 5-5 5" stroke="#0b4279" stroke-width="2.2" fill="none"/></svg></div>

<!-- footer -->
<svg class="abs foot-wave" width="1200" height="80" viewBox="0 0 1200 80">
  <path d="M0 0 Q600 60 1200 6 L1200 16 Q600 62 0 20Z" fill="#0b4279"/>
  <path d="M0 38 Q600 92 1200 30 L1200 80 L0 80Z" fill="#0b4279"/>
</svg>
<div class="abs footer"></div>
<div class="abs foot-brand"><span class="brand-dot"></span><span class="brand-name">FELDMOOR</span></div>
<div class="abs updates">GET OUR LATEST UPDATES</div>
<div class="abs email">Email ID<span class="send"><svg width="18" height="18" viewBox="0 0 16 16"><path d="M15 1L1 7l6 2 2 6z" fill="#fff"/></svg></span></div>
<div class="abs foot-rule" style="top:2330px"></div>

<div class="abs col-h" style="left:111px">ABOUT US</div>
<div class="abs contact" style="top:2420px"><svg width="20" height="26" viewBox="0 0 20 26" fill="none" stroke="#b38d48" stroke-width="1.5"><path d="M10 25s8-9 8-15a8 8 0 0 0-16 0c0 6 8 15 8 15z"/><circle cx="10" cy="10" r="3"/></svg><span>Feldmoor,<br>Address Comes Here</span></div>
<div class="abs contact" style="top:2494px"><svg width="20" height="20" viewBox="0 0 20 20" fill="none" stroke="#b38d48" stroke-width="1.5"><path d="M4 2l4 4-2 2c1 3 3 5 6 6l2-2 4 4-3 3C8 18 2 12 1 5z"/></svg><span>ph +1 555 014 2273</span></div>
<div class="abs contact" style="top:2538px"><svg width="22" height="18" viewBox="0 0 22 18" fill="none" stroke="#b38d48" stroke-width="1.5"><rect x="1" y="2" width="20" height="14"/><path d="M1 2l10 8 10-8"/></svg><span>info@feldmoor.com</span></div>

<div class="abs col-h" style="left:419px">ABOUT US</div>
<p class="abs about-text">Nemo enim ipsam voluptatem quia voluptas sit aspernatur aut odit aut fugit, sed quia emo enim ipsam voluptatem quia voluptas sit aspernatur aut odit aut fugit, sed</p>
<div class="abs follow"><span class="col-h">FOLLOW US</span><div class="social"><span></span><span></span></div></div>

<div class="abs col-h" style="left:740px">QUICK LINKS</div>
<ul class="abs links" style="left:740px"><li>Home</li><li>About</li><li>My List</li><li>News</li><li>Categories</li></ul>

<div class="abs col-h" style="left:969px">OTHER LINKS</div>
<ul class="abs links" style="left:969px"><li>Tearms</li><li>Privacy Policy</li><li>FAQ</li><li>Contact us</li></ul>

<div class="abs foot-rule" style="top:2613px"></div>
<div class="abs copy">2022 Feldmoor.All Rghts Reserved.</div>

</body>
</html>
```